Mobile app for deals

Mobile App Name: Vanta 6 Mirk

Design screen shots for the issue of quotes for deals.

1. Loading screen
2. User signs in with credentials or signs up
2. Search by category
3. Search by location
4. Create a project

The expected experience after a project is placed:
- Project alerted
- Quotes
- Project complete
- Rating
- Payment

#TotallyExcited
Updates

Project Deadline Extended Reason: Deadline has been extended on request from a few designers who saw the project late and who would like to submit designs.Thank you to all who submitted on time, we are reviewing your designs and will respond shortly. Added Monday, June 29, 2015

Target Market(s)

Contractors market

Industry/Entity Type

Business Directory

Font styles to use
Sans Serif

Requirements
Must have
• Simple design
• User friendly
• Translateable (later)

```html
<!DOCTYPE html>
<html lang="en">
<head>
<meta charset="utf-8">
<title>Vanta 6 Mirk – Sign in</title>
<link rel="stylesheet" href="https://fonts.googleapis.com/css2?family=Poppins:wght@300;400;500;600&display=swap">
<style>
  :root {
    --brand-blue: #1a5e9a;
    --ink-white: #ffffff;
    --rule-white: rgba(255, 255, 255, 0.9);
  }
  * { box-sizing: border-box; margin: 0; padding: 0; }
  html, body {
    width: 675px;
    height: 1200px;
    overflow: hidden;
    background: var(--brand-blue);
  }
  .screen {
    position: relative;
    width: 675px;
    height: 1200px;
    background: var(--brand-blue);
    color: var(--ink-white);
    font-family: "Poppins", sans-serif;
  }
  .app-name {
    position: absolute;
    top: 230px;
    left: 0;
    width: 100%;
    text-align: center;
    font-weight: 500;
    font-size: 36px;
    letter-spacing: 0.5px;
    line-height: 52px;
  }
  .field {
    position: absolute;
    left: 117px;
    width: 440px;
    height: 66px;
    border-top: 1px solid var(--rule-white);
    border-bottom: 1px solid var(--rule-white);
  }
  .field-email { top: 446px; }
  .field-password { top: 554px; }
  .field-label {
    position: absolute;
    left: 17px;
    top: 8px;
    font-weight: 300;
    font-size: 39px;
    line-height: 48px;
  }
  .submit-button {
    position: absolute;
    left: 279px;
    top: 738px;
    width: 117px;
    height: 117px;
  }
  .footer {
    position: absolute;
    left: 0;
    top: 1100px;
    width: 100%;
    height: 100px;
    border-top: 1px solid var(--rule-white);
  }
  .register-link {
    position: absolute;
    top: 36px;
    left: 0;
    width: 100%;
    text-align: center;
    font-weight: 300;
    font-size: 21px;
    line-height: 30px;
  }
  .register-link .network-name {
    font-weight: 600;
    font-size: 24px;
  }
</style>
</head>
<body>
  <main class="screen">
    <h1 class="app-name">Vanta 6 Mirk</h1>

    <div class="field field-email">
      <span class="field-label">E-mail</span>
    </div>
    <div class="field field-password">
      <span class="field-label">Password</span>
    </div>

    <svg class="submit-button" viewBox="0 0 117 117" role="img" aria-label="Sign in">
      <circle cx="58.5" cy="58.5" r="58" fill="none" stroke="#ffffff" stroke-width="1"/>
      <polyline points="48,27 78,58.5 48,90" fill="none" stroke="#ffffff" stroke-width="2"/>
    </svg>

    <footer class="footer">
      <p class="register-link">register with <span class="network-name">Linkora</span></p>
    </footer>
  </main>
</body>
</html>
```